A boutique/architectural website for a landscape company

I'm after a minimilstic boutique website for my landscape design and construction business. I have been exploring Wix and created some pages on that but want something more aesthetic.

Industry/Entity Type

Landscaping design and construction

Number of Pages Required

5+ page

Font styles to use
Sans Serif

Colors

Designer to choose colors to be used in the design.

Requirements
Must have
• an architectural, minimalistic look
Nice to have
• Simplicitly and nice images
Should not have
• A corporate look

```html
<!DOCTYPE html>
<html lang="en">
<head>
<meta charset="utf-8">
<title>Verdant Grove — Landscaping &amp; Design</title>
<link rel="stylesheet" href="https://fonts.googleapis.com/css2?family=League+Spartan:wght@300;400;500;600;700&display=swap">
<style>
:root{
  --green:#0c5c4d;
  --green-dark:#08463b;
  --ink:#2b2b2b;
  --text:#555;
  --muted:#8a8a8a;
  --light:#f4f4f4;
  --footer:#e9e9e9;
  --white:#fff;
}
*{box-sizing:border-box;margin:0;padding:0}
html,body{width:1200px;height:4202px;overflow:hidden}
body{position:relative;font-family:"League Spartan",sans-serif;color:var(--ink);background:var(--white)}
.abs{position:absolute}
.btn{position:absolute;display:flex;align-items:center;justify-content:center;background:var(--green);color:var(--white);border-radius:22px;font-size:14px;font-weight:400;letter-spacing:.3px}
.photo{position:absolute}

/* top bar & nav */
.topbar{left:0;top:0;width:1200px;height:28px;background:var(--green)}
.topbar .call{position:absolute;left:686px;top:8px;font-size:11px;color:#d6e6e2}
.topbar .call b{color:var(--white);font-weight:500}
.social-dot{position:absolute;width:10px;height:10px;border-radius:50%;border:1.5px solid var(--white)}
.nav{left:0;top:28px;width:1200px;height:75px;background:var(--white);box-shadow:0 2px 6px rgba(0,0,0,.08)}
.logo-box{left:174px;top:0;width:141px;height:124px;background:var(--white);z-index:5;box-shadow:0 2px 6px rgba(0,0,0,.1);display:flex;flex-direction:column;align-items:center;justify-content:center;gap:8px}
.logo-mark{width:26px;height:26px;border-radius:50%;background:var(--green)}
.logo-name{font-size:17px;font-weight:500;color:var(--green);letter-spacing:2px}
.menu{position:absolute;top:60px;font-size:13px;color:#555;letter-spacing:.3px}
.menu.active{color:var(--green);border-bottom:1.5px solid var(--green);padding-bottom:2px}

/* hero */
.hero{left:0;top:103px;width:1200px;height:607px;background:linear-gradient(120deg,#3f4a2c 0%,#7a6a55 30%,#a87e62 50%,#4d6d32 75%,#2f4d24 100%)}
.hero-title{left:192px;top:286px;font-size:49px;font-weight:700;color:var(--white);letter-spacing:.5px}
.hero-sub{left:192px;top:344px;font-size:45px;font-weight:400;color:var(--white)}
.arrow-circle{position:absolute;border-radius:50%;display:flex;align-items:center;justify-content:center}
.service-circle{position:absolute;width:202px;height:202px;border-radius:50%;border:5px solid var(--white);box-shadow:0 4px 10px rgba(0,0,0,.25)}
.service-title{position:absolute;width:300px;text-align:center;font-size:18px;font-weight:600;color:var(--ink);line-height:23px;letter-spacing:.4px}
.service-title.accent{color:var(--green)}
.service-text{position:absolute;width:240px;text-align:center;font-size:11.5px;line-height:19px;color:var(--text)}

/* about */
.about-label{left:725px;top:1189px;font-size:19px;font-weight:600;color:var(--ink)}
.about-title{left:725px;top:1211px;font-size:44px;font-weight:600;color:var(--ink)}
.about-lead{left:725px;top:1268px;width:300px;font-size:15px;line-height:23px;color:var(--text)}
.about-text{left:725px;top:1323px;width:285px;font-size:11.5px;line-height:20px;color:var(--text)}

/* projects */
.projects{left:0;top:1625px;width:1200px;height:790px;background:linear-gradient(180deg,#e9ece9 0%,#dfe4df 60%,#cfd6cf 100%)}
.section-label{position:absolute;width:1200px;left:0;text-align:center;font-size:19px;font-weight:500;color:var(--ink)}
.section-title{position:absolute;width:1200px;left:0;text-align:center;font-size:44px;font-weight:600;color:var(--ink)}
.tile{position:absolute;border:4px solid var(--white);box-shadow:0 2px 6px rgba(0,0,0,.15);display:flex;align-items:flex-end;justify-content:center;padding-bottom:22px;color:var(--white);font-size:15px;font-weight:500;letter-spacing:.4px}

/* cta band */
.cta{left:0;top:2415px;width:1200px;height:455px;background:linear-gradient(180deg,#dfe6e4 0%,#c9d3c4 45%,#7f9a5c 75%,#6f7f4a 100%)}
.cta-title{left:0;width:1200px;top:2490px;text-align:center;font-size:35px;font-weight:600;color:var(--ink)}
.cta-sub{left:0;width:1200px;top:2540px;text-align:center;font-size:31px;font-weight:400;color:var(--ink)}
.cta-text{left:340px;width:520px;top:2594px;text-align:center;font-size:14px;line-height:23px;color:#333}

/* testimonials */
.card{position:absolute;width:393px;height:255px;background:var(--white);box-shadow:0 3px 12px rgba(0,0,0,.12)}
.card .pic{position:absolute;left:0;top:0;width:166px;height:255px}
.quote-mark{position:absolute;left:190px;top:20px;font-size:46px;font-weight:700;color:var(--green);line-height:46px}
.card .lead{position:absolute;left:190px;top:60px;width:185px;font-size:15px;line-height:22px;color:var(--ink)}
.card .body{position:absolute;left:190px;top:134px;width:185px;font-size:11px;line-height:18px;color:var(--text)}
.card .name{position:absolute;left:190px;top:224px;font-size:11px;font-weight:600;color:var(--green)}

/* contact */
.contact{left:0;top:3372px;width:1200px;height:492px;background:linear-gradient(90deg,#23331c 0%,#3c5a2a 40%,#5f7a3a 70%,#7b6a45 100%)}
.field{position:absolute;left:192px;width:408px;border:1.5px solid rgba(255,255,255,.85)}
.field-label{position:absolute;left:20px;top:-9px;padding:0 6px;font-size:11px;letter-spacing:1px;color:rgba(255,255,255,.85);background:transparent}
.field-value{position:absolute;left:36px;font-size:13px;letter-spacing:1px;color:var(--white)}

/* footer */
.footer{left:0;top:3864px;width:1200px;height:272px;background:var(--footer)}
.footer-logo{left:196px;top:3920px;width:141px;display:flex;flex-direction:column;align-items:center;gap:8px}
.divider{position:absolute;top:3918px;width:1px;height:180px;background:#cfcfcf}
.f-head{position:absolute;top:3937px;font-size:15px;color:var(--green)}
.f-head::before{content:"";position:absolute;left:0;top:-12px;width:28px;height:2px;background:var(--green)}
.f-list{position:absolute;font-size:11px;line-height:21px;color:#555;list-style:none}
.f-item{position:absolute;font-size:11px;line-height:16px;color:#555;display:flex;gap:10px}
.f-social{position:absolute;width:22px;height:22px;border-radius:50%;background:var(--green)}
.newsletter{position:absolute;left:861px;top:4068px;width:145px;height:28px;background:var(--white);border:1px solid #ddd;font-size:9px;color:#888;padding:9px 10px}
.newsletter-btn{position:absolute;left:979px;top:4068px;width:27px;height:28px;background:var(--green);display:flex;align-items:center;justify-content:center}
.bottom-bar{left:0;top:4136px;width:1200px;height:66px;background:var(--footer);border-top:1px solid #d6d6d6}
.bottom-bar span{position:absolute;top:24px;font-size:11px;color:#777}
</style>
</head>
<body>

<!-- header -->
<div class="abs topbar">
  <div class="call">CALL US : <b>01 234 5678 9</b></div>
  <div class="social-dot" style="left:975px;top:9px"></div>
  <div class="social-dot" style="left:994px;top:9px"></div>
  <div class="social-dot" style="left:1020px;top:9px"></div>
</div>
<div class="abs nav">
  <span class="menu active" style="left:449px;top:31px">HOME</span>
  <span class="menu" style="left:515px;top:31px">ABOUT US</span>
  <span class="menu" style="left:606px;top:31px">SERVICES</span>
  <span class="menu" style="left:693px;top:31px">OUR WORKS</span>
  <span class="menu" style="left:798px;top:31px">CONTACT US</span>
  <div class="btn" style="left:921px;top:22px;width:116px;height:29px;font-size:13px">Get A Quote</div>
</div>
<div class="abs logo-box">
  <div class="logo-mark"></div>
  <div class="logo-name">VERDANT GROVE</div>
</div>

<!-- hero -->
<div class="photo hero" role="img" aria-label="Gardener laying fresh turf beside a brick-paved garden path"></div>
<svg class="abs" style="left:0;top:600px" width="1200" height="115" viewBox="0 0 1200 115">
  <path d="M0 110 C300 20 800 -5 1200 110 L1200 115 L0 115 Z" fill="var(--white)"/>
  <path d="M0 110 C300 20 800 -5 1200 110" fill="none" stroke="var(--green)" stroke-width="3"/>
</svg>
<div class="abs hero-title">MAKE YOUR LAWN</div>
<div class="abs hero-sub">Clean &amp; Beautiful</div>
<div class="btn" style="left:192px;top:434px;width:194px;height:44px;font-size:15px">CONTACT US NOW</div>
<div class="arrow-circle" style="left:1088px;top:345px;width:42px;height:42px;background:var(--white)">
  <svg width="14" height="14" viewBox="0 0 14 14"><path d="M5 2 L10 7 L5 12" fill="none" stroke="#555" stroke-width="2"/></svg>
</div>
<div class="arrow-circle" style="left:72px;top:345px;width:42px;height:42px;background:rgba(255,255,255,.2)">
  <svg width="14" height="14" viewBox="0 0 14 14"><path d="M9 2 L4 7 L9 12" fill="none" stroke="rgba(255,255,255,.5)" stroke-width="2"/></svg>
</div>

<!-- services -->
<div class="service-circle" role="img" aria-label="Gardener laying turf rolls" style="left:204px;top:608px;background:linear-gradient(135deg,#b08d6e,#5d7d3a 60%,#2f5a2a)"></div>
<div class="service-circle" role="img" aria-label="Stone paving slabs set in artificial grass" style="left:499px;top:574px;background:linear-gradient(180deg,#4f7a35 0%,#b8b9b4 45%,#8c8d88 100%)"></div>
<div class="service-circle" role="img" aria-label="Renovated garden with lawn and stepping stones" style="left:791px;top:608px;background:linear-gradient(180deg,#6b7a62 0%,#5b8a37 55%,#7cb342 100%)"></div>

<div class="service-title" style="left:155px;top:836px">GARDENING AND<br>LANDSCAPING</div>
<div class="service-text" style="left:185px;top:888px">Lorem ipsum dolor sit amet, consectetur adipiscing elit. Mauris in rhoncus orci. Pellentesque ac consequat nulla.</div>
<div class="service-title accent" style="left:450px;top:806px">PAVINGT WORK</div>
<div class="service-text" style="left:480px;top:836px">Lorem ipsum dolor sit amet, consectetur adipiscing elit. Mauris in rhoncus orci. Pellentesque ac consequat nulla.</div>
<div class="service-title" style="left:742px;top:836px">RENOVATIONS INSIDE<br>AND OUT SIDE</div>
<div class="service-text" style="left:772px;top:888px">Lorem ipsum dolor sit amet, consectetur adipiscing elit. Mauris in rhoncus orci. Pellentesque ac consequat nulla.</div>
<div class="btn" style="left:515px;top:963px;width:170px;height:35px">CONTACT US NOW</div>

<!-- about -->
<div class="abs" style="left:665px;top:1104px;width:90px;height:45px;background:var(--green-dark)"></div>
<div class="photo" role="img" aria-label="Gardener handing a potted flowering plant to a woman in a garden" style="left:192px;top:1104px;width:473px;height:424px;background:linear-gradient(110deg,#c9c2b4 0%,#6f6a4f 35%,#8a4a3e 60%,#4e6e2a 100%)"></div>
<div class="abs about-label">ABOUT US</div>
<div class="abs about-title">WHO WE ARE</div>
<div class="abs about-lead">Lorem ipsum dolor sit amet, consectetur adipiscing elit.</div>
<div class="abs about-text">Lorem ipsum dolor sit amet, consectetur adipiscing elit. Proin massa augue, aliquet eu magna congue malesuada enim. Etiam in rutrum est. Donec vel lobortis purus, eget posuere massa.</div>
<div class="btn" style="left:725px;top:1431px;width:142px;height:35px">LEARN MORE</div>

<!-- projects -->
<div class="photo projects" role="img" aria-label="Faded view of a suburban garden and trees"></div>
<div class="section-label" style="top:1685px">PROJECTS</div>
<div class="section-title" style="top:1706px">RECENT PROJECTS</div>

<div class="tile" role="img" aria-label="Stepping stone slabs across a lawn" style="left:152px;top:1800px;width:287px;height:244px;background:linear-gradient(180deg,#5f8b3c,#a3a7a0 60%,#5d7d3a)">LOREM IPSUM</div>
<div class="tile" role="img" aria-label="Patio seating area surrounded by planting" style="left:458px;top:1800px;width:285px;height:165px;background:linear-gradient(135deg,#4a7a2e,#9b8f5e 55%,#5a7d33)">LOREM IPSUM</div>
<div class="tile" role="img" aria-label="Curved brick driveway beside a lawn" style="left:765px;top:1800px;width:287px;height:244px;background:linear-gradient(180deg,#9fb6a6 0%,#5e8f3a 30%,#54504a 60%,#3e3b37 100%)">LOREM IPSUM</div>
<div class="tile" role="img" aria-label="Pruning shears trimming a hedge" style="left:152px;top:2064px;width:287px;height:206px;background:linear-gradient(135deg,#3c6b22,#6e9c3d 50%,#2f4f1d)">LOREM IPSUM</div>
<div class="tile" role="img" aria-label="Garden steps and curved path through a lawn" style="left:458px;top:1984px;width:285px;height:286px;background:linear-gradient(180deg,#2f4e22,#4f7a31 45%,#8a8d84 70%,#4d8a2c)">LOREM IPSUM</div>
<div class="tile" role="img" aria-label="Sunlit garden lawn with stone path" style="left:765px;top:2064px;width:287px;height:206px;background:linear-gradient(180deg,#d09a3e 0%,#6a8a34 40%,#3f5f24 100%)">LOREM IPSUM</div>
<div class="btn" style="left:507px;top:2315px;width:186px;height:35px">VIEW ALL PROJECTS</div>

<!-- call to action -->
<div class="photo cta" role="img" aria-label="Rooftop garden terrace with lounge seating overlooking a city"></div>
<div class="abs cta-title">WE TAKE CARE OF YOUR LANDSCAPE.</div>
<div class="abs cta-sub">YOU TAKE BACK YOUR FREE TIME.</div>
<div class="abs cta-text">Lorem ipsum dolor sit amet, consectetur adipiscing elit. Proin massa augue, aliquet eu magna congue malesuada enim. Etiam in rutrum est. Donec vel lobortis purus, eget posuere massa.</div>
<div class="btn" style="left:507px;top:2684px;width:186px;height:36px">CONTACT US TODAY!</div>

<!-- testimonials -->
<div class="section-label" style="top:2921px">TESTIMONIALS</div>
<div class="section-title" style="top:2950px">WHAT CLIENTS SAY</div>

<div class="card" style="left:189px;top:3029px">
  <div class="pic" role="img" aria-label="Client standing in a greenhouse with flower pots" style="background:linear-gradient(180deg,#8aa07a,#c56a2e 55%,#d8d3ca)"></div>
  <div class="quote-mark">&ldquo;</div>
  <div class="lead">Lorem ipsum dolor sit amet consectetur adipiscing elit.</div>
  <div class="body">Nam hendrerit diam nec dolor iaculis euismod. Phasellus non nunc nisl. Aenean bibendum acc umsan pharetra.</div>
  <div class="name">Mara Linfield</div>
</div>
<div class="card" style="left:616px;top:3029px">
  <div class="pic" role="img" aria-label="Gardener in an apron watering plants" style="background:linear-gradient(180deg,#6e7a6a,#9a8a70 55%,#4f6a3a)"></div>
  <div class="quote-mark">&ldquo;</div>
  <div class="lead">Integer cursus vest ulum interdum. Mauris sto libero!</div>
  <div class="body">Morbi luctus convallis ipsum eg et blandit. Donec iaculis ac velit sed placerat. In porttitor dictum nunc eget.</div>
  <div class="name">Owen Carrow</div>
</div>
<div class="arrow-circle" style="left:1050px;top:3134px;width:46px;height:46px;border:1.5px solid #333;background:var(--white)">
  <svg width="14" height="14" viewBox="0 0 14 14"><path d="M5 2 L10 7 L5 12" fill="none" stroke="#333" stroke-width="2"/></svg>
</div>

<!-- contact form -->
<div class="photo contact" role="img" aria-label="Smiling gardener holding hedge shears in a green garden"></div>
<div class="field" style="top:3486px;height:44px">
  <span class="field-label" style="top:-16px">YOUR NAME</span>
  <span class="field-value" style="top:14px;left:34px">DANIEL HARTLEY &nbsp;&nbsp; |</span>
</div>
<div class="field" style="top:3554px;height:44px">
  <span class="field-label" style="top:-16px">EMAIL</span>
</div>
<div class="field" style="top:3624px;height:111px">
  <span class="field-label" style="top:-16px">MESSAGE</span>
</div>
<div class="btn" style="left:429px;top:3719px;width:156px;height:34px">SEND MESSAGE</div>

<!-- footer -->
<div class="abs footer"></div>
<div class="abs footer-logo">
  <div class="logo-mark"></div>
  <div class="logo-name">VERDANT GROVE</div>
</div>
<div class="btn" style="left:194px;top:4053px;width:145px;height:31px">CONTACT US NOW</div>
<div class="divider" style="left:383px"></div>
<div class="divider" style="left:549px"></div>
<div class="divider" style="left:805px"></div>

<div class="f-head" style="left:435px">Site Links</div>
<ul class="f-list" style="left:435px;top:3968px">
  <li>Home</li><li>About Us</li><li>Services</li><li>Our Work</li><li>Contact Us</li>
</ul>

<div class="f-head" style="left:593px">Contact Us</div>
<div class="f-item" style="left:593px;top:3976px">
  <svg width="13" height="13" viewBox="0 0 24 24"><path d="M6 2 L9 2 L11 7 L8.5 9 C10 12 12 14 15 15.5 L17 13 L22 15 L22 18 C22 20 20 22 18 22 C9 21 3 15 2 6 C2 4 4 2 6 2Z" fill="none" stroke="var(--green)" stroke-width="2"/></svg>
  <span>Phone: 210 555 04821</span>
</div>
<div class="f-item" style="left:593px;top:4008px;width:175px">
  <svg width="13" height="13" viewBox="0 0 24 24" style="flex:none"><path d="M12 22 C7 16 4 12 4 9 A8 8 0 0 1 20 9 C20 12 17 16 12 22Z" fill="none" stroke="var(--green)" stroke-width="2"/><circle cx="12" cy="9" r="3" fill="none" stroke="var(--green)" stroke-width="2"/></svg>
  <span>Address: 48 Willow Lane, Suite 7, Fernbrook, Oregon</span>
</div>
<div class="f-item" style="left:593px;top:4068px">
  <svg width="13" height="13" viewBox="0 0 24 24"><rect x="2" y="5" width="20" height="14" fill="none" stroke="var(--green)" stroke-width="2"/><path d="M2 5 L12 13 L22 5" fill="none" stroke="var(--green)" stroke-width="2"/></svg>
  <span>Email: hello@verdantgrove.test</span>
</div>

<div class="f-head" style="left:861px">Get Connected</div>
<div class="f-social" style="left:861px;top:3966px"></div>
<div class="f-social" style="left:887px;top:3966px"></div>
<div class="f-social" style="left:913px;top:3966px"></div>
<div class="f-head" style="left:861px;top:4040px">Newsletter</div>
<div class="newsletter">Email..</div>
<div class="newsletter-btn">
  <svg width="13" height="13" viewBox="0 0 24 24"><path d="M2 11 L22 2 L15 22 L11 13 Z" fill="var(--white)"/></svg>
</div>

<div class="abs bottom-bar">
  <span style="left:194px">@2021 Verdant Grove Landscaping | All Rights Reserved.</span>
  <span style="left:815px">Terms &amp; Conditions &nbsp;| &nbsp;Privacy Policy</span>
</div>

</body>
</html>
```